Redfield interiors PTY LTD

My business specializes in commercial fitout which builds walls, ceilings, doors, uses also materials aluminium in works. Id like to have a logo designed for my company too.

Industry/Entity Type

Business

```html
<!DOCTYPE html>
<html lang="en">
<head>
<meta charset="utf-8">
<title>Redfield Interiors – Business Card</title>
<link rel="stylesheet" href="https://fonts.googleapis.com/css2?family=Montserrat:wght@700&family=Open+Sans:wght@400;600&display=swap">
<style>
  :root {
    --backdrop: #dcdcdc;
    --blue-light: #1d8fde;
    --blue-deep: #0b5aa3;
    --blue-text: #0f63b0;
    --ink: #3b3f44;
    --paper: #ffffff;
  }
  * { margin: 0; padding: 0; box-sizing: border-box; }
  html, body {
    width: 1200px; height: 852px; overflow: hidden;
    background: var(--backdrop);
  }
  .sheet {
    position: relative; width: 1200px; height: 852px;
    display: flex; align-items: center; justify-content: center; gap: 40px;
  }
  .card {
    position: relative; width: 520px; height: 300px;
    border-radius: 22px; overflow: hidden;
  }
  .card--back {
    background: linear-gradient(200deg, var(--blue-light) 0%, var(--blue-deep) 100%);
    display: flex; align-items: center; justify-content: center;
  }
  .wordmark {
    font-family: "Montserrat", sans-serif; font-weight: 700;
    display: flex; align-items: center; gap: 14px;
  }
  .wordmark__dot { border-radius: 50%; flex: none; }
  .wordmark__text { display: flex; flex-direction: column; line-height: 1; }
  .wordmark__name { letter-spacing: 0.5px; }
  .wordmark__sub { letter-spacing: 0.62em; }

  .card--back .wordmark { color: var(--paper); }
  .card--back .wordmark__dot { width: 22px; height: 22px; background: var(--paper); }
  .card--back .wordmark__name { font-size: 42px; }
  .card--back .wordmark__sub { font-size: 15px; margin-top: 6px; }

  .card--front { background: var(--paper); }
  .card--front .wordmark {
    position: absolute; top: 30px; right: 34px; color: var(--blue-text);
  }
  .card--front .wordmark__dot { width: 14px; height: 14px; background: var(--blue-text); }
  .card--front .wordmark__name { font-size: 30px; }
  .card--front .wordmark__sub { font-size: 11px; margin-top: 4px; }

  .person {
    position: absolute; top: 108px; right: 34px; text-align: right;
    font-family: "Open Sans", sans-serif;
  }
  .person__name { font-size: 20px; font-weight: 600; color: var(--blue-text); }
  .person__role { font-size: 11px; color: var(--ink); }

  .contact {
    position: absolute; bottom: 30px; right: 34px; list-style: none;
    font-family: "Open Sans", sans-serif; font-size: 13px; color: var(--ink);
    text-align: right; line-height: 1.45;
  }
  .contact__address { margin-bottom: 6px; }
  .contact__item { display: flex; justify-content: flex-end; align-items: center; gap: 6px; }
  .contact__icon { width: 12px; height: 12px; fill: var(--blue-text); flex: none; }
</style>
</head>
<body>
<main class="sheet">
  <section class="card card--back" aria-label="Card reverse">
    <div class="wordmark">
      <span class="wordmark__dot"></span>
      <span class="wordmark__text">
        <span class="wordmark__name">REDFIELD</span>
        <span class="wordmark__sub">INTERIORS</span>
      </span>
    </div>
  </section>

  <section class="card card--front" aria-label="Card front">
    <div class="wordmark">
      <span class="wordmark__dot"></span>
      <span class="wordmark__text">
        <span class="wordmark__name">REDFIELD</span>
        <span class="wordmark__sub">INTERIORS</span>
      </span>
    </div>

    <div class="person">
      <p class="person__name">Mark Ellison</p>
      <p class="person__role">Managing Director</p>
    </div>

    <ul class="contact">
      <li class="contact__address">18 Harlow Lane,<br>Westbrook, US 204817</li>
      <li class="contact__item">555.014.2290
        <svg class="contact__icon" viewBox="0 0 12 12" aria-hidden="true"><path d="M2.5 1 4.5 1 5.3 3.4 4.1 4.4Q5 6.8 7.6 7.9L8.6 6.7 11 7.5 11 9.5Q11 11 9.5 11 1 10.3 1 2.5 1 1 2.5 1Z"/></svg>
      </li>
      <li class="contact__item">mark@redfield.test
        <svg class="contact__icon" viewBox="0 0 12 12" aria-hidden="true"><path d="M1 2.5h10v7H1z M1.6 3 6 6.4 10.4 3" fill="none" stroke="#0f63b0" stroke-width="1.2"/></svg>
      </li>
      <li class="contact__item">www.redfield.test
        <svg class="contact__icon" viewBox="0 0 12 12" aria-hidden="true"><g fill="none" stroke="#0f63b0" stroke-width="1"><circle cx="6" cy="6" r="5"/><ellipse cx="6" cy="6" rx="2.2" ry="5"/><path d="M1 6h10"/></g></svg>
      </li>
    </ul>
  </section>
</main>
</body>
</html>
```